Ridgeline Orchards Organic Cherry POS card 7x11

We are wanting to create a one-sided 7 x 11 organic cherry card that is eye catching and informative.This should be clear and easy to read and not cluttered. We use these cards as a display in grocery stores, demo stands, and other events to market Organic Ridgeline Sweet Orchards. We have a few facts that we would like displayed on the card (see attachment).

Target Market(s)

Consumers

Industry/Entity Type

Agriculture

Requirements
Must have
• Natural color palettes
• Easy to read
• Ridgeline Orchards
Nice to have
• Unique, realistic cherry design

```html
<!DOCTYPE html>
<html lang="en">
<head>
<meta charset="utf-8">
<title>Ridgeline Orchards – Organic Cherry Card</title>
<link rel="stylesheet" href="https://fonts.googleapis.com/css2?family=Josefin+Sans:wght@600&family=Dancing+Script:wght@700&display=swap">
<style>
  :root {
    --paper: #ffffff;
    --wash-light: #eef8dc;
    --wash-mid: #d6efb4;
    --burgundy: #7a1c3e;
    --dash: #6a1e34;
    --leaf-green: #6f8f1a;
    --cherry-light: #e4242c;
    --cherry-mid: #c8121c;
    --cherry-deep: #8e0a14;
  }
  html, body {
    margin: 0;
    padding: 0;
    overflow: hidden;
    background: var(--paper);
  }
  .card {
    position: relative;
    width: 1200px;
    height: 880px;
    overflow: hidden;
    background: var(--paper);
    font-family: "Josefin Sans", sans-serif;
  }
  .wash {
    position: absolute;
    border-radius: 46% 54% 50% 50% / 55% 45% 55% 45%;
    filter: blur(8px);
  }
  .wash--left {
    left: -40px; top: 60px; width: 640px; height: 560px;
    background: radial-gradient(ellipse at 45% 45%, var(--wash-mid) 0%, var(--wash-light) 55%, rgba(238,248,220,0) 75%);
  }
  .wash--right {
    left: 580px; top: 55px; width: 640px; height: 760px;
    background: radial-gradient(ellipse at 50% 55%, var(--wash-mid) 0%, var(--wash-light) 55%, rgba(238,248,220,0) 76%);
  }
  .facts {
    position: absolute;
    left: 20px;
    top: 0;
    width: 604px;
    margin: 0;
    text-align: center;
    color: var(--burgundy);
    font-weight: 600;
    font-size: 32px;
    letter-spacing: 0.34em;
    text-transform: uppercase;
  }
  .facts span {
    position: absolute;
    left: 0; right: 0;
    line-height: 1;
    padding-left: 0.34em;
  }
  .cherry-photo {
    position: absolute;
    left: 622px; top: 200px;
    width: 566px; height: 312px;
    border-radius: 42% 40% 46% 50% / 46% 38% 62% 58%;
    background:
      radial-gradient(circle at 30% 40%, rgba(255,255,255,0.18) 0%, rgba(255,255,255,0) 18%),
      radial-gradient(circle at 72% 35%, rgba(255,255,255,0.16) 0%, rgba(255,255,255,0) 16%),
      radial-gradient(ellipse at 50% 45%, var(--cherry-light) 0%, var(--cherry-mid) 55%, var(--cherry-deep) 100%);
  }
  .guide {
    position: absolute;
    left: 0; top: 0;
    pointer-events: none;
  }
  .benefits {
    position: absolute;
    left: 652px;
    top: 578px;
    width: 440px;
    margin: 0;
    padding: 0;
    list-style: none;
    text-align: center;
    font-family: "Dancing Script", cursive;
    font-weight: 700;
    font-size: 33px;
    line-height: 33px;
    color: var(--leaf-green);
  }
  .brand {
    position: absolute;
    left: 52px;
    top: 682px;
    display: flex;
    align-items: center;
    gap: 24px;
  }
  .brand__dot {
    width: 68px; height: 68px;
    border-radius: 50%;
    background: var(--burgundy);
  }
  .brand__name {
    font-family: "Josefin Sans", sans-serif;
    font-weight: 600;
    font-size: 44px;
    letter-spacing: 0.06em;
    color: var(--burgundy);
  }
</style>
</head>
<body>
<main class="card">
  <div class="wash wash--left" aria-hidden="true"></div>
  <div class="wash wash--right" aria-hidden="true"></div>

  <h1 class="facts">
    <span style="top:118px">Organic</span>
    <span style="top:162px">Ridgeline Cherries</span>
    <span style="top:220px">Make up 1/3</span>
    <span style="top:279px">of the nation's</span>
    <span style="top:322px">production.</span>
    <span style="top:404px">Washington State</span>
    <span style="top:448px">is the nation's</span>
    <span style="top:491px">largest producer</span>
    <span style="top:535px">of organic</span>
    <span style="top:578px">cherries.</span>
  </h1>

  <div class="cherry-photo" role="img" aria-label="Photograph of a cluster of glossy red sweet cherries with green stems"></div>

  <svg class="guide" width="1200" height="880" viewBox="0 0 1200 880" aria-hidden="true">
    <ellipse cx="874" cy="330" rx="250" ry="222" fill="none" stroke="var(--dash)" stroke-width="5" stroke-dasharray="22 14"/>
    <path d="M 1040 496 Q 1085 545 1068 592 T 1028 660" fill="none" stroke="var(--dash)" stroke-width="5" stroke-dasharray="22 14"/>
  </svg>

  <ul class="benefits">
    <li>Health benefits:</li>
    <li>Fat Free</li>
    <li>Source of Vitamin C</li>
    <li>A Natural Anti-Inflammatory</li>
    <li>Source of Potassium</li>
    <li>Source of Melatonin</li>
  </ul>

  <div class="brand">
    <div class="brand__dot" aria-hidden="true"></div>
    <div class="brand__name">Ridgeline Orchards</div>
  </div>
</main>
</body>
</html>
```